Business Card Design Project

I want a cleaner business card and envelope then what we have now, its too crowded.
Updates

I update with logo, this can be changed anyway you feel it looks best. I also have put gaurantee on there and extended time, this is my first time doing this. Also gave an example of current card

Target Market(s)

a wide array of customers from lattice 700 to small companies and cleints

Industry/Entity Type

Business

Requirements
Must have
• Need to have address, telephone number email
Nice to have
• a sharp professional card that stands out but is still very clean.
Should not have
• Not crazy looking

```html
<!DOCTYPE html>
<html lang="en">
<head>
<meta charset="utf-8">
<title>Halvorne Insurance Group – Business Card</title>
<link href="https://fonts.googleapis.com/css2?family=Didact+Gothic&family=EB+Garamond:wght@400&display=swap" rel="stylesheet">
<style>
  :root {
    --ink: #2a0d0f;
    --card: #ffffff;
    --band-dark: #2b0c0e;
    --stage-top: #2e0b0d;
    --stage-mid: #9b2a30;
    --stage-red: #8c161c;
    --floor: #333333;
    --mark-grey: #8c8c8c;
    --label: #4a2a2a;
  }
  * { margin: 0; padding: 0; box-sizing: border-box; }
  html, body { width: 1200px; height: 900px; overflow: hidden; background: #fff; }
  body { font-family: "Didact Gothic", "Century Gothic", sans-serif; color: var(--ink); position: relative; }

  .board-header { position: absolute; left: 0; top: 0; width: 1200px; height: 212px; background: #fff; }
  .brand-square { position: absolute; background: var(--mark-grey); }
  .brand-name { position: absolute; color: var(--ink); font-weight: 400; line-height: 1; white-space: nowrap; }

  .header-square { left: 212px; top: 32px; width: 150px; height: 151px; }
  .header-name-main { left: 396px; top: 32px; font-size: 90px; letter-spacing: 26px; }
  .header-name-sub { left: 399px; top: 125px; font-size: 42px; letter-spacing: 16px; }

  .stage { position: absolute; left: 0; top: 212px; width: 1200px; height: 446px;
    background: linear-gradient(180deg, var(--stage-top) 0%, #5a1419 30%, var(--stage-mid) 62%, #c96a6e 82%, #fff 100%); }
  .floor-band { position: absolute; left: 0; top: 658px; width: 1200px; height: 190px;
    background: linear-gradient(180deg, var(--stage-red) 0%, #7a1318 55%, #4a0c10 100%); }
  .footer-band { position: absolute; left: 0; top: 848px; width: 1200px; height: 52px; background: var(--floor); }

  .card { position: absolute; top: 273px; width: 511px; height: 294px; background: var(--card);
    box-shadow: 4px 8px 14px rgba(0,0,0,.45); overflow: hidden; }
  .card-front { left: 62px; }
  .card-back { left: 636px; width: 510px; }
  .card-band { position: absolute; left: 0; bottom: 0; width: 100%; height: 18px; background: var(--band-dark); }

  .front-square { left: 0; top: 0; width: 228px; height: 234px; }
  .front-name-main { left: 10px; top: 237px; font-size: 24px; letter-spacing: 7px; }
  .front-name-sub { left: 11px; top: 261px; font-size: 12px; letter-spacing: 4.4px; }

  .contact { position: absolute; left: 251px; top: 3px; font-size: 14px; line-height: 17px; color: var(--ink); }
  .contact-name { margin-top: 28px; font-size: 15px; font-weight: 700; -webkit-text-stroke: .3px var(--ink); }
  .contact-title { font-size: 14px; letter-spacing: .3px; }
  .contact-address { margin-top: 23px; }
  .contact-lines { margin-top: 23px; }

  .back-square { left: 62px; top: 37px; width: 75px; height: 75px; }
  .back-name-main { left: 153px; top: 40px; font-size: 41px; letter-spacing: 14.5px; }
  .back-name-sub { left: 155px; top: 83px; font-size: 20px; letter-spacing: 8.3px; }

  .service-col { position: absolute; font-size: 12px; line-height: 14px; letter-spacing: .2px; color: var(--ink); }
  .service-col h3 { font-weight: 400; font-size: 14px; line-height: 16px; letter-spacing: 0; -webkit-text-stroke: .3px var(--ink); }
  .service-col ul { list-style: none; }
  .service-col li::before { content: "• "; }
  .col-left { left: 66px; top: 138px; }
  .col-left .group + .group { margin-top: 5px; }
  .col-right { left: 283px; top: 138px; font-size: 12.5px; }
  .col-right li { line-height: 17.4px; }
  .col-right li.wrap { line-height: 14px; padding-top: 3px; }
  .col-right li.wrap span { display: block; padding-left: 7px; }

  .card-label { position: absolute; top: 598px; font-family: "EB Garamond", Georgia, serif; font-size: 16px; letter-spacing: 2px; color: var(--label); }
  .label-front { left: 86px; }
  .label-back { left: 659px; }
</style>
</head>
<body>
  <header class="board-header">
    <div class="brand-square header-square"></div>
    <div class="brand-name header-name-main">HALVORNE</div>
    <div class="brand-name header-name-sub">INSURANCE GROUP</div>
  </header>

  <div class="stage"></div>
  <div class="floor-band"></div>
  <div class="footer-band"></div>

  <section class="card card-front" aria-label="Card front">
    <div class="brand-square front-square"></div>
    <div class="brand-name front-name-main">HALVORNE</div>
    <div class="brand-name front-name-sub">INSURANCE GROUP</div>
    <div class="contact">
      <div class="contact-name">Nora Whitfield</div>
      <div class="contact-title">OPERATIONS MANAGER</div>
      <div class="contact-address">
        Halvorne Insurance Group<br>
        18240 Harbor Ridge Avenue<br>
        Lakeview Heights, Mi. 48000
      </div>
      <div class="contact-lines">
        P: 555-014-2291 ext. 418<br>
        F: 555-014-2298<br>
        E: nwhitfield@halvorneagency.com<br>
        W: www.halvorneagency.com
      </div>
    </div>
    <div class="card-band"></div>
  </section>

  <section class="card card-back" aria-label="Card back">
    <div class="brand-square back-square"></div>
    <div class="brand-name back-name-main">HALVORNE</div>
    <div class="brand-name back-name-sub">INSURANCE GROUP</div>

    <div class="service-col col-left">
      <div class="group">
        <h3>COMMERCIAL INSURANCE</h3>
        <ul>
          <li>Traditional Insurance Coverage</li>
          <li>Executive Protection Coverage</li>
          <li>Specialty Coverage Insurance</li>
        </ul>
      </div>
      <div class="group">
        <h3>PERSONAL INSURANCE</h3>
        <ul>
          <li>Auto/Recretional/Boat</li>
          <li>Home/Renters/Condo</li>
          <li>Umbrella Liability</li>
        </ul>
      </div>
    </div>

    <div class="service-col col-right">
      <h3>EMPLOYEE BENEFITS</h3>
      <ul>
        <li>Voluntary Benefits</li>
        <li>Disability Insurance</li>
        <li>Prescription Coverage</li>
        <li>Medical/Dental/Optical Plans</li>
        <li class="wrap">Life &amp; Accidental Death &amp;<span>Dismemberment Insurance</span></li>
      </ul>
    </div>
    <div class="card-band"></div>
  </section>

  <div class="card-label label-front">FRONT</div>
  <div class="card-label label-back">BACK</div>
</body>
</html>
```